Documentary Movie Needs a Poster

We need a poster/lobby card for a documentary film made by six filmmakers. Lobby card needs to list name of sponsor, names of filmmakers and (if feasible, but not required) image frames from each of the six sections of the film.

Text should be very readable. OK to have all caps text or upper/lower.

Design comps are OK, these do not need to be print-ready final images.

Target Market(s)

well educated documentary filmgoers

Industry/Entity Type

Movie

Requirements
Must have
• Must contain the following text (please use helvetica neue or similar font).

Please use the following sponsor name:

The
Marlowe Institute for Cinema
presents

Please use the following filmmaker names:

Theodore Pelusky
Robert Nash
Frederick Tamworth
Harold E. F. Pratt
Vincent Lorimer
Danny Frost

Please use the 6 images in archive/zip to create the card.

You can also do text-only versions of the card (no images).

Card needs to be 2:1 aspect ratio (2000px wide x 1000 pixels high)

Names of filmmakers should each be same size (no filmmaker has visual priority over the other).

Colors for text, lines and other design elements should be Ash, Iron and/or Salt.

Feel free to crop images if you need to.

```html
<!DOCTYPE html>
<html lang="en">
<head>
<meta charset="utf-8">
<title>Ash, Iron and/or Salt. — Lobby Card</title>
<link rel="stylesheet" href="https://fonts.googleapis.com/css2?family=Exo+2:ital,wght@1,900&display=swap">
<style>
  :root {
    --card-blue: #4070b5;
    --ink: #000000;
  }
  * { margin: 0; padding: 0; box-sizing: border-box; }
  html, body {
    width: 1200px;
    height: 685px;
    overflow: hidden;
    background: var(--card-blue);
  }
  .lobby-card {
    position: relative;
    width: 1200px;
    height: 685px;
    overflow: hidden;
    background: var(--card-blue);
    color: var(--ink);
    font-family: "Exo 2", "Helvetica Neue", Arial, sans-serif;
    font-style: italic;
    font-weight: 900;
  }
  .presenter {
    position: absolute;
    left: 306px;
    top: 50px;
    font-size: 44px;
    line-height: 35px;
    font-variant: small-caps;
    letter-spacing: -0.8px;
  }
  .presenter span { display: block; }
  .soldier-figure {
    position: absolute;
    left: 80px;
    top: 188px;
    width: 255px;
    height: 405px;
    background: var(--ink);
    border-radius: 60px 60px 10px 10px;
  }
  .film-title {
    position: absolute;
    left: 380px;
    top: 288px;
    font-size: 70px;
    line-height: 56px;
    text-transform: uppercase;
    letter-spacing: -0.5px;
  }
  .film-title span { display: block; }
  .filmmakers {
    position: absolute;
    top: 494px;
    list-style: none;
    font-size: 37px;
    line-height: 34px;
    font-variant: small-caps;
    letter-spacing: -0.6px;
    white-space: nowrap;
  }
  .filmmakers--left { left: 398px; }
  .filmmakers--right { left: 803px; }
</style>
</head>
<body>
  <main class="lobby-card">
    <p class="presenter">
      <span>The</span>
      <span>Marlowe Institute</span>
      <span>for Cinema</span>
      <span>presents</span>
    </p>

    <div class="soldier-figure" role="img" aria-label="Black silhouette of a kneeling soldier in helmet and combat gear"></div>

    <h1 class="film-title">
      <span>Ash, Iron</span>
      <span>and/or Salt.</span>
    </h1>

    <ul class="filmmakers filmmakers--left">
      <li>Theodore Pelusky</li>
      <li>Robert Nash</li>
      <li>Frederick Tamworth</li>
    </ul>
    <ul class="filmmakers filmmakers--right">
      <li>Harold E. F. Pratt</li>
      <li>Vincent Lorimer</li>
      <li>Danny Frost</li>
    </ul>
  </main>
</body>
</html>
```